Business card for Eyelash extension salon in Beverly Hills,California USA

We need new business card for our salon in Beverly Hills. The salon name is 'Lumarra' . We would like to have...Business name: Lumarra Name of person: will provide later Address 6128 N.Corbel Ridge Blvd Westmere Vale , CA 90000 Phone: will provide later (Text only) Web: www.lumarrastudio-example.com Pictogrid icon, Friendvale icon follow us for seasonal campaign and news @lumarrastudioexample Design should look elegant, high-end, clean, simple, cohesive with my brand. Please refer my brand board. Business name color will be metallic bronzy color. Im thinking grey background or white background. Thanks

Target Market(s)

25-35. Gender neutral. People who are in Entertainment business industry.
This is High-end Eyelash extension salon in Beverly Hills

Industry/Entity Type

Beauty Salon

Contact Information for Business Card

Business name: Lumarra
Name of person: will provide later
Address 6128 N.Corbel Ridge Blvd Westmere Vale , CA 90000
Phone: will provide later (Text only)
Web: www.lumarrastudio-example.com
Pictogrid icon, Friendvale icon
follow us for seasonal campaign and news @lumarrastudioexample

Requirements
Must have
• Beautiful, elegant, clean and simple look but very attractive and modern
Should not have
• We don't like too clutter, too busy designs.

```html
<!DOCTYPE html>
<html lang="en">
<head>
<meta charset="utf-8">
<title>Lumarra – Business Card</title>
<link href="https://fonts.googleapis.com/css2?family=Signika:wght@400;500&display=swap" rel="stylesheet">
<style>
  :root {
    --page: #ffffff;
    --card-grey: #1b1b1b;
    --card-black: #000000;
    --bronze: #8a6a52;
    --gold-text: #c9955c;
    --shadow: rgba(0, 0, 0, 0.55);
  }
  html, body {
    margin: 0;
    padding: 0;
    width: 1200px;
    height: 1000px;
    overflow: hidden;
    background: var(--page);
    font-family: "Signika", sans-serif;
  }
  .canvas {
    position: relative;
    width: 1200px;
    height: 1000px;
  }
  .card {
    position: absolute;
    left: 293px;
    width: 635px;
    height: 363px;
    overflow: hidden;
    background: var(--card-grey);
    box-shadow: -6px 8px 10px var(--shadow);
  }
  .card-front { top: 73px; }
  .card-back { top: 551px; }
  .wave {
    position: absolute;
    left: 0;
    top: 0;
    width: 635px;
    height: 363px;
  }
  .wave path { fill: var(--card-black); }
  .brand-name {
    position: absolute;
    color: var(--bronze);
    font-weight: 400;
    white-space: nowrap;
    margin: 0;
    line-height: 1;
  }
  .card-front .brand-name {
    left: 0;
    width: 635px;
    text-align: center;
    top: 70px;
    font-size: 104px;
    letter-spacing: 2px;
  }
  .card-back .brand-name {
    left: 26px;
    top: 38px;
    font-size: 56px;
    letter-spacing: 1px;
  }
  .follow-line {
    position: absolute;
    left: 0;
    width: 635px;
    top: 314px;
    text-align: center;
    color: var(--gold-text);
    font-size: 16px;
    font-weight: 400;
    margin: 0;
  }
  .contact-list {
    position: absolute;
    left: 40px;
    top: 163px;
    margin: 0;
    padding: 0;
    list-style: none;
  }
  .contact-item {
    display: flex;
    align-items: center;
    height: 30px;
    color: var(--gold-text);
    font-size: 16px;
    font-weight: 400;
  }
  .contact-icon {
    width: 20px;
    height: 20px;
    margin-right: 9px;
    flex: none;
    fill: var(--gold-text);
  }
  .social-row { gap: 16px; margin-top: 2px; }
  .social-tag { display: flex; align-items: center; gap: 6px; }
  .social-mark-square {
    width: 14px; height: 14px; background: var(--gold-text);
  }
  .social-mark-circle {
    width: 14px; height: 14px; border-radius: 50%; background: var(--gold-text);
  }
</style>
</head>
<body>
<div class="canvas">

  <section class="card card-front" aria-label="Card front">
    <svg class="wave" viewBox="0 0 635 363" aria-hidden="true">
      <path d="M0 224 C90 214 160 240 220 260 C330 240 420 214 507 215 C570 216 610 222 635 227 V363 H0 Z"/>
    </svg>
    <h1 class="brand-name">Lumarra</h1>
    <p class="follow-line">Follow us for seasonal campaign and news @lumarrastudioexample</p>
  </section>

  <section class="card card-back" aria-label="Card back">
    <svg class="wave" viewBox="0 0 635 363" aria-hidden="true">
      <path d="M0 0 H635 V141 C590 140 520 125 415 103 C300 120 180 145 87 147 C50 147 20 144 0 139 Z"/>
    </svg>
    <h2 class="brand-name">Lumarra</h2>
    <ul class="contact-list">
      <li class="contact-item">
        <svg class="contact-icon" viewBox="0 0 20 20" aria-label="Phone"><path d="M4.5 3 L7.5 2 L9.5 6 L7.5 7.5 C8.5 10 10 11.5 12.5 12.5 L14 10.5 L18 12.5 L17 15.5 C10 16.5 3.5 10 4.5 3 Z"/></svg>
      </li>
      <li class="contact-item">
        <svg class="contact-icon" viewBox="0 0 20 20" aria-label="Email"><text x="10" y="16" text-anchor="middle" font-size="19" font-weight="500" font-family="Signika, sans-serif">@</text></svg>
      </li>
      <li class="contact-item">
        <svg class="contact-icon" viewBox="0 0 20 20" aria-label="Address"><path d="M10 2 L19 10 H16 V18 H12 V13 H8 V18 H4 V10 H1 Z"/></svg>
        <span>6128 N.Corbel Ridge Blvd Westmere Vale , CA 90000</span>
      </li>
      <li class="contact-item">
        <svg class="contact-icon" viewBox="0 0 20 20" aria-label="Website"><g fill="none" stroke="#c9955c" stroke-width="1.6"><circle cx="10" cy="10" r="8.5"/><ellipse cx="10" cy="10" rx="4" ry="8.5"/><path d="M1.5 10 H18.5 M3 5.5 H17 M3 14.5 H17"/></g></svg>
        <span>www.lumarrastudio-example.com</span>
      </li>
      <li class="contact-item social-row">
        <span class="social-tag"><span class="social-mark-square"></span>Friendvale</span>
        <span class="social-tag"><span class="social-mark-circle"></span>Pictogrid</span>
      </li>
    </ul>
  </section>

</div>
</body>
</html>
```